Business cards, Stationary, E-mail signature, leterhead, fax coversheet, thank you card, invoice tem
Torvan Networks Stationary - please read brief
Business cards, Stationary, E-mail signature, leterhead, fax coversheet, thank you card, invoice tem -
Creative Brief
Use specific fonts
Use the best that will go with the logo design
Professional
Brent Oakley
71523 Birch Ridge Court, Suite 204 Sterling, VA 20783
BrentO@torvannetworks.example
www.torvannetworks.example
Use the icon on the left side of the logo only

```html
<!DOCTYPE html>
<html lang="en">
<head>
<meta charset="utf-8">
<title>Torvan Networks Business Cards</title>
<link href="https://fonts.googleapis.com/css2?family=Montserrat:wght@500;700;800&family=Open+Sans:wght@400;600;700&display=swap" rel="stylesheet">
<style>
  :root {
    --bg: #e9e7e4;
    --card: #ffffff;
    --navy: #1f2f6b;
    --blue: #2c4aa0;
    --blue-light: #5a7fd0;
    --grey-text: #4a4d55;
    --grey-line: #c9ccd2;
    --grey-band: #b7bbc3;
  }
  * { margin: 0; padding: 0; box-sizing: border-box; }
  html, body { width: 1200px; height: 852px; overflow: hidden; }
  body {
    background: var(--bg);
    position: relative;
    font-family: "Open Sans", Arial, sans-serif;
    color: var(--grey-text);
  }
  .card {
    position: absolute;
    width: 500px;
    height: 286px;
    background: var(--card);
    border-radius: 14px;
    overflow: hidden;
    box-shadow: 0 6px 18px rgba(0,0,0,0.18);
  }
  .card--split { left: 80px; top: 110px; }
  .card--stacked { left: 620px; top: 456px; }

  .swoosh { position: absolute; left: 0; bottom: 0; width: 500px; height: 80px; }

  .brand { position: absolute; display: flex; flex-direction: column; align-items: flex-start; }
  .brand__row { display: flex; align-items: center; gap: 10px; }
  .brand__dot { width: 34px; height: 34px; border-radius: 50%; background: var(--blue); flex: none; }
  .brand__name {
    font-family: "Montserrat", Arial, sans-serif;
    font-weight: 800;
    color: var(--navy);
    font-size: 25px;
    line-height: 1;
    letter-spacing: 0.5px;
    text-transform: uppercase;
  }
  .brand__tagline {
    margin-top: 6px;
    font-size: 7px;
    letter-spacing: 0.6px;
    color: var(--grey-text);
    text-transform: uppercase;
    white-space: nowrap;
  }

  .holder { font-family: "Montserrat", Arial, sans-serif; font-weight: 700; color: var(--navy); font-size: 14px; }
  .address { font-size: 11px; line-height: 1.5; margin-top: 14px; }
  .contacts { list-style: none; font-size: 11px; line-height: 1.65; }
  .contacts li { display: flex; align-items: center; gap: 7px; white-space: nowrap; }
  .contacts svg { width: 11px; height: 11px; flex: none; }

  /* split card: stacked brand to the left of the divider */
  .card--split .brand { left: 16px; top: 42px; width: 200px; align-items: center; }
  .card--split .brand__row { flex-direction: column; gap: 8px; }
  .card--split .brand__dot { width: 48px; height: 48px; }
  .card--split .brand__name { font-size: 26px; line-height: 1.05; text-align: center; max-width: 200px; }
  .card--split .divider {
    position: absolute; left: 232px; top: 26px; width: 1px; height: 170px; background: var(--grey-line);
  }
  .card--split .details { position: absolute; left: 248px; top: 30px; }
  .card--split .contacts { margin-top: 14px; }

  /* stacked card */
  .card--stacked .brand { left: 48px; top: 40px; }
  .card--stacked .holder-block { position: absolute; left: 48px; top: 112px; text-align: right; width: 190px; }
  .card--stacked .holder-block .address { margin-top: 10px; }
  .card--stacked .contacts { position: absolute; left: 262px; top: 100px; }
</style>
</head>
<body>

<svg width="0" height="0" style="position:absolute">
  <defs>
    <linearGradient id="band-blue" x1="0" y1="0" x2="1" y2="0">
      <stop offset="0" stop-color="#1c2f74"/>
      <stop offset="0.55" stop-color="#3456b2"/>
      <stop offset="1" stop-color="#6c8fdc"/>
    </linearGradient>
    <symbol id="icon-phone" viewBox="0 0 24 24">
      <path d="M6.6 10.8a15 15 0 0 0 6.6 6.6l2.2-2.2a1 1 0 0 1 1-.25 11.4 11.4 0 0 0 3.6.57 1 1 0 0 1 1 1V20a1 1 0 0 1-1 1A17 17 0 0 1 3 4a1 1 0 0 1 1-1h3.5a1 1 0 0 1 1 1c0 1.25.2 2.45.57 3.570a1 1 0 0 1-.25 1z" fill="#1f2f6b"/>
    </symbol>
    <symbol id="icon-fax" viewBox="0 0 24 24">
      <rect x="6" y="2" width="12" height="7" fill="#1f2f6b"/>
      <rect x="2" y="9" width="20" height="10" rx="2" fill="#1f2f6b"/>
      <rect x="6" y="15" width="12" height="7" fill="#fff" stroke="#1f2f6b" stroke-width="2"/>
    </symbol>
    <symbol id="icon-at" viewBox="0 0 24 24">
      <circle cx="12" cy="12" r="4" fill="none" stroke="#1f2f6b" stroke-width="2.6"/>
      <path d="M16 8v5.5a2.5 2.5 0 0 0 5 0V12a9 9 0 1 0-3.5 7.1" fill="none" stroke="#1f2f6b" stroke-width="2.6"/>
    </symbol>
    <symbol id="icon-web" viewBox="0 0 24 24">
      <circle cx="12" cy="12" r="10" fill="#9aa0ab"/>
    </symbol>
    <symbol id="swoosh" viewBox="0 0 500 80">
      <path d="M0 40 C140 62 330 52 500 14 L500 80 L0 80 Z" fill="var(--grey-band)" opacity="0.55"/>
      <path d="M0 50 C150 70 340 60 500 26 L500 80 L0 80 Z" fill="url(#band-blue)"/>
      <path d="M0 50 C150 70 340 60 500 26" fill="none" stroke="#ffffff" stroke-width="1.5" opacity="0.7"/>
    </symbol>
  </defs>
</svg>

<section class="card card--split" aria-label="Business card, split layout">
  <div class="brand">
    <div class="brand__row">
      <span class="brand__dot"></span>
      <span class="brand__name">Torvan Networks</span>
    </div>
    <span class="brand__tagline">IT | Management Consulting | Staffing</span>
  </div>
  <div class="divider"></div>
  <div class="details">
    <p class="holder">Brent Oakley</p>
    <p class="address">71523 Birch Ridge Court,<br>Suite 204, Sterling, VA 20783</p>
    <ul class="contacts">
      <li><svg><use href="#icon-phone"/></svg>703 555 0148</li>
      <li><svg><use href="#icon-fax"/></svg>703 555 0162</li>
      <li><svg><use href="#icon-at"/></svg>BrentO@torvannetworks.example</li>
      <li><svg><use href="#icon-web"/></svg>www.torvannetworks.example</li>
    </ul>
  </div>
  <svg class="swoosh"><use href="#swoosh"/></svg>
</section>

<section class="card card--stacked" aria-label="Business card, stacked layout">
  <div class="brand">
    <div class="brand__row">
      <span class="brand__dot"></span>
      <span class="brand__name">Torvan Networks</span>
    </div>
    <span class="brand__tagline">IT | Management Consulting | Staffing</span>
  </div>
  <div class="holder-block">
    <p class="holder">Brent Oakley</p>
    <p class="address">71523 Birch Ridge Court,<br>Suite 204, Sterling, VA 20783</p>
  </div>
  <ul class="contacts">
    <li><svg><use href="#icon-phone"/></svg>703 555 0148</li>
    <li><svg><use href="#icon-fax"/></svg>703 555 0162</li>
    <li><svg><use href="#icon-at"/></svg>BrentO@torvannetworks.example</li>
    <li><svg><use href="#icon-web"/></svg>www.torvannetworks.example</li>
  </ul>
  <svg class="swoosh"><use href="#swoosh"/></svg>
</section>

</body>
</html>
```